Business Card Re-Design for a Lighting Designer

I would like my business card re-designed. It is currently high gloss and they scratch too easily. I don not think the current design lends itself well to a matte finish. I have included the current design for reference along with our company logo.
Check out our website for current branding.
http://www.brenmoorastudio.example

Updates
Some of the top contenders are muslim and it is a holiday for them. I do not want to discriminate and would expect the same courtesy for holidays we celebrate.
Target Market(s)
Interior Designers, Architects
Contact Information for Business Card
Logo - Name, Title, Address, Telephone Number and Extension, Email
Font styles to use
Requirements
Must have
- All the information listed on the current business card. If you use Red, it needs to be the red from our logo.
Nice to have
- Vertical and Horizontal Designs will be entertained.
Should not have
- Requirements for a glossy finish...should not look too corporate since we are a design firm.

```html
<!DOCTYPE html>
<html lang="en">
<head>
<meta charset="utf-8">
<title>Bren Moora Studio – Business Card</title>
<link rel="stylesheet" href="https://fonts.googleapis.com/css2?family=Arimo:wght@400;700&display=swap">
<style>
  :root {
    --backdrop: #e9e9e9;
    --paper: #ffffff;
    --brand-red: #9e1b16;
    --grey-mid: #9a9a9a;
    --grey-light: #bdbdbd;
    --ink: #1c1c1c;
  }
  * { margin: 0; padding: 0; box-sizing: border-box; }
  html, body {
    width: 1200px;
    height: 800px;
    overflow: hidden;
    background: var(--backdrop);
    font-family: "Arimo", Arial, sans-serif;
  }
  .sheet {
    position: relative;
    width: 1200px;
    height: 800px;
  }
  .card {
    position: absolute;
    top: 278px;
    width: 420px;
    height: 240px;
    background: var(--paper);
    overflow: hidden;
  }
  .card--back { left: 142px; }
  .card--front { left: 638px; }
  .card__arcs {
    position: absolute;
    inset: 0;
    width: 100%;
    height: 100%;
  }
  .contact {
    position: absolute;
    left: 150px;
    top: 45px;
    color: var(--paper);
    font-size: 13px;
    line-height: 16px;
    white-space: nowrap;
  }
  .contact__name {
    font-weight: 700;
    letter-spacing: 0.01em;
  }
  .contact__block { margin-top: 24px; }
  .contact__block + .contact__block { margin-top: 9px; }
  .identity {
    position: absolute;
    left: 46px;
    top: 33px;
  }
  .identity__square {
    width: 64px;
    height: 64px;
    background: var(--brand-red);
  }
  .identity__name {
    margin-top: 14px;
    font-size: 26px;
    line-height: 28px;
    font-weight: 400;
    color: var(--ink);
    text-transform: uppercase;
  }
</style>
</head>
<body>
<main class="sheet">

  <section class="card card--back" aria-label="Business card, contact side">
    <svg class="card__arcs" viewBox="0 0 525 300" preserveAspectRatio="none" aria-hidden="true">
      <path d="M85 0 Q-42 124 163 300 L525 300 L525 0 Z" fill="var(--grey-light)"/>
      <path d="M113 0 Q27 124 173 300 L525 300 L525 0 Z" fill="var(--grey-mid)"/>
      <path d="M178 0 Q65 124 203 300 L525 300 L525 0 Z" fill="var(--brand-red)"/>
    </svg>
    <div class="contact">
      <p class="contact__name">MARA ELLISON</p>
      <p class="contact__title">Principal</p>
      <div class="contact__block">
        <p>217 Alder Row, Suite 40</p>
        <p>Atlanta, Georgia 30312 USA</p>
      </div>
      <div class="contact__block">
        <p>404 555 0148 x1</p>
        <p>www.brenmoorastudio.example</p>
        <p>mara@brenmoorastudio.example</p>
      </div>
    </div>
  </section>

  <section class="card card--front" aria-label="Business card, identity side">
    <svg class="card__arcs" viewBox="0 0 525 300" preserveAspectRatio="none" aria-hidden="true">
      <circle cx="322" cy="150" r="168" fill="var(--brand-red)"/>
      <circle cx="267" cy="150" r="181" fill="var(--grey-light)"/>
      <circle cx="212" cy="150" r="196" fill="var(--grey-mid)"/>
      <circle cx="127" cy="150" r="239" fill="var(--paper)"/>
    </svg>
    <div class="identity">
      <div class="identity__square"></div>
      <p class="identity__name">Bren Moora<br>Studio</p>
    </div>
  </section>

</main>
</body>
</html>
```